Fashion Show Invitation image/Design

looking for a cover image for a Fashion Show Invitation. Something that conveys the beauty of spring. not sure if there should be a "magical" component. just want something elegant that can be used on an invitation and save the date etc. Looking to use spring pastel colors (pinks, purples etc... like spring flowers) I don't need a full invitation design, just an image we can use to convey our "theme"
We are an non profit Philanthropy group and this is our major fundraiser.
The only text should be:
The Harwell Circle Presents A Night in Silk
Target Market(s)
fashion show invitees
Industry/Entity Type
Fashion
Requirements
Must have
- spring colors.. pastels, flowers etc
- text= The Harwell Circle Presents A Night in Silk
Nice to have
- some sort of innuendo or implication of magic? im not sure about this.
Should not have
- dark colors

```html
<!DOCTYPE html>
<html lang="en">
<head>
<meta charset="utf-8">
<title>The Harwell Circle Presents A Night in Silk</title>
<link rel="stylesheet" href="https://fonts.googleapis.com/css2?family=Jost:wght@300;400;700&display=swap">
<style>
  :root {
    --page-bg: #f3f3f3;
    --card-edge: #ffffff;
    --sky-blue: #7f9ff0;
    --sky-lavender: #b9a4f2;
    --sky-pink: #f0b4ea;
    --silk-light: #45bfe9;
    --silk-deep: #1a8fd0;
    --type: #ffffff;
  }
  * { margin: 0; padding: 0; box-sizing: border-box; }
  html, body {
    width: 1200px;
    height: 848px;
    overflow: hidden;
    background: var(--page-bg);
  }
  .stage {
    position: relative;
    width: 1200px;
    height: 848px;
  }
  .invitation-cover {
    position: absolute;
    left: 364px;
    top: 77px;
    width: 472px;
    height: 695px;
    border: 3px solid var(--card-edge);
    overflow: hidden;
    font-family: "Jost", "Futura", sans-serif;
    color: var(--type);
    text-align: center;
  }
  .cover-backdrop {
    position: absolute;
    inset: 0;
    background:
      radial-gradient(ellipse 60% 30% at 85% 6%, rgba(250, 190, 240, 0.9), transparent 70%),
      linear-gradient(180deg,
        var(--sky-blue) 0%,
        var(--sky-lavender) 28%,
        var(--sky-pink) 50%,
        var(--sky-lavender) 62%,
        var(--silk-light) 74%,
        var(--silk-deep) 100%);
  }
  .host-name {
    position: absolute;
    top: 168px;
    left: 0;
    right: 0;
    font-weight: 400;
    font-size: 31px;
    letter-spacing: 0.5px;
    line-height: 1;
  }
  .presents {
    position: absolute;
    top: 208px;
    left: 0;
    right: 0;
    font-weight: 400;
    font-size: 17px;
    letter-spacing: 0.5px;
    line-height: 1;
  }
  .event-title {
    position: absolute;
    top: 240px;
    left: 0;
    right: 0;
    font-weight: 300;
    font-size: 98px;
    line-height: 84px;
    letter-spacing: -2px;
  }
  .event-title .title-line { display: block; }
  .event-title strong { font-weight: 700; }
  .title-reflection {
    position: absolute;
    top: 408px;
    left: 0;
    right: 0;
    font-weight: 300;
    font-size: 98px;
    line-height: 84px;
    letter-spacing: -2px;
    transform: scaleY(-1);
    transform-origin: top;
    opacity: 0.55;
    -webkit-mask-image: linear-gradient(0deg, rgba(0,0,0,0.8) 55%, transparent 85%);
    mask-image: linear-gradient(0deg, rgba(0,0,0,0.8) 55%, transparent 85%);
    height: 84px;
    top: 492px;
  }
</style>
</head>
<body>
  <main class="stage">
    <section class="invitation-cover">
      <div class="cover-backdrop" role="img" aria-label="Pastel pink and lavender spring sky above billowing folds of turquoise silk"></div>
      <p class="host-name">THE HARWELL CIRCLE</p>
      <p class="presents">PRESENTS</p>
      <h1 class="event-title">
        <span class="title-line">A <strong>NIGHT</strong></span>
        <span class="title-line">IN SILK</span>
      </h1>
      <div class="title-reflection" aria-hidden="true">IN SILK</div>
    </section>
  </main>
</body>
</html>
```